Redesign Business Cards, Attached

Please read instructions carefully. If you have any questions send a message before submitting your ONE design. Please redesign attached business cards. Double sided. Use same content and descriptions. Use black, silver, crimson red and gold colors. My only issue with the attached design is the background colors. I like the layout as-is. I can provide the individual pictures on the back side later. Do not submit more than one design. One submission shall include both front and back. Do not submit front and back separately. A second project will be launched to create a matching post card after completion of this.
Industry/Entity Type
see description and attachments.
Contact Information for Business Card
Requirements
Must have
- see description and attachments.
Nice to have
Should not have

```html
<!DOCTYPE html>
<html lang="en">
<head>
<meta charset="utf-8">
<title>Harbor Line Boat Training – Business Card</title>
<link href="https://fonts.googleapis.com/css2?family=Montserrat:wght@500;600;700;800&display=swap" rel="stylesheet">
<style>
  :root{
    --ink:#141414;
    --charcoal:#2a2a2c;
    --gold:#d4a945;
    --gold-soft:#e2bf6a;
    --crimson:#a3122a;
    --silver:#c4c7cb;
    --silver-light:#8e9297;
    --white:#ffffff;
    --backdrop:#d4d5d1;
  }
  *{box-sizing:border-box;margin:0;padding:0}
  html,body{width:1200px;height:801px;overflow:hidden}
  body{background:var(--backdrop);font-family:"Montserrat",sans-serif;position:relative}
  .card{position:absolute;top:240px;width:560px;height:320px;overflow:hidden;
        box-shadow:0 14px 30px rgba(0,0,0,.25);background:var(--white)}
  .card--front{left:27px}
  .card--back{left:613px}

  .sea-photo{position:absolute;left:0;top:0;width:100%;
             background:linear-gradient(160deg,var(--silver-light) 0%,var(--charcoal) 55%,var(--ink) 100%)}
  .card--front .sea-photo{height:100%}
  .card--back .sea-photo{height:150px}

  .front-panel{position:absolute;inset:0}
  .contact{position:absolute;left:262px;top:28px;width:285px;color:var(--ink)}
  .contact__name{font-weight:800;font-size:20px;letter-spacing:.5px;white-space:nowrap}
  .contact__role{font-weight:500;font-size:15px;line-height:1.25;margin-top:4px}
  .contact__pill{display:inline-flex;align-items:center;gap:8px;margin-top:12px;
        background:var(--ink);color:var(--gold-soft);border-radius:18px;padding:6px 16px;
        font-weight:600;font-size:15px;white-space:nowrap}
  .contact__pill svg{width:14px;height:14px}
  .contact__line{display:flex;align-items:center;gap:7px;margin-top:10px;font-weight:500;font-size:13px}
  .contact__line + .contact__line{margin-top:4px}
  .contact__line svg{width:13px;height:13px;flex:none}

  .brand-seal{position:absolute;left:32px;top:166px;width:140px;height:140px;border-radius:50%;
        background:var(--white);border:5px solid var(--gold);display:flex;align-items:center;justify-content:center;text-align:center;
        color:var(--ink);font-weight:800;font-size:16px;line-height:1.2}

  .badge{position:absolute;width:56px;height:56px;border-radius:50%;
         box-shadow:0 2px 6px rgba(0,0,0,.3)}
  .badge--gold{left:150px;top:62px;background:var(--gold)}
  .badge--red{left:220px;top:56px;background:var(--crimson)}
  .badge--silver{left:290px;top:50px;background:var(--silver)}

  .services{position:absolute;left:26px;top:164px;display:flex;gap:10px}
  .services__col{display:flex;flex-direction:column;gap:9px}
  .services__col:nth-child(2){margin-top:-12px}
  .services__col:nth-child(3){margin-top:-24px}
  .services__col:nth-child(4){margin-top:-36px}
  .service{width:116px;height:60px;border-radius:8px;display:flex;align-items:center;justify-content:center;
           text-align:center;font-weight:600;font-size:12.5px;line-height:1.1;padding:4px}
  .service--dark{background:var(--ink);color:var(--white)}
  .service--gold{background:var(--gold);color:var(--ink)}
  .service--small{font-size:11px}
  .back-url{position:absolute;right:40px;bottom:12px;color:var(--crimson);font-weight:600;font-size:15px;letter-spacing:2px}
</style>
</head>
<body>

<section class="card card--front" aria-label="Business card front">
  <div class="sea-photo" role="img" aria-label="Photo of a center-console boat speeding across open water"></div>
  <svg class="front-panel" viewBox="0 0 560 320" aria-hidden="true">
    <polygon points="214,0 240,0 240,30 214,48" fill="var(--crimson)"/>
    <polygon points="240,0 560,0 560,200 420,262 240,200" fill="var(--gold)" stroke="var(--silver)" stroke-width="9"/>
    <polygon points="380,262 420,262 420,300" fill="var(--crimson)"/>
  </svg>
  <div class="contact">
    <div class="contact__name">JORDAN R. CALLOWAY</div>
    <div class="contact__role">USCG Licensed Captain<br>Certified Instructor</div>
    <div class="contact__pill">TEXT
      <svg viewBox="0 0 24 24"><path fill="currentColor" d="M6.6 10.8a15.1 15.1 0 0 0 6.6 6.6l2.2-2.2a1 1 0 0 1 1-.25 11.4 11.4 0 0 0 3.6.57 1 1 0 0 1 1 1V20a1 1 0 0 1-1 1A17 17 0 0 1 3 4a1 1 0 0 1 1-1h3.5a1 1 0 0 1 1 1c0 1.25.2 2.45.57 3.57a1 1 0 0 1-.25 1z"/></svg>
      (555) 014-2290</div>
    <div class="contact__line">
      <svg viewBox="0 0 24 24"><rect x="3" y="5" width="18" height="14" rx="1" fill="none" stroke="currentColor" stroke-width="2"/><path d="M3 6l9 7 9-7" fill="none" stroke="currentColor" stroke-width="2"/></svg>
      hello@helmandtide.com</div>
    <div class="contact__line">
      <svg viewBox="0 0 24 24"><circle cx="12" cy="12" r="9" fill="none" stroke="currentColor" stroke-width="2"/><path d="M3 12h18M12 3c3 3 3 15 0 18M12 3c-3 3-3 15 0 18" fill="none" stroke="currentColor" stroke-width="1.6"/></svg>
      www.helmandtide.com</div>
  </div>
  <div class="brand-seal">Harbor Line<br>Boat Training</div>
</section>

<section class="card card--back" aria-label="Business card back">
  <div class="sea-photo" role="img" aria-label="Photo of a boat cutting through open water"></div>
  <div class="badge badge--gold" aria-hidden="true"></div>
  <div class="badge badge--red" aria-hidden="true"></div>
  <div class="badge badge--silver" aria-hidden="true"></div>
  <div class="services">
    <div class="services__col">
      <div class="service service--dark">Hands-on<br>Boat<br>Training</div>
      <div class="service service--gold">Island<br>Anchoring</div>
    </div>
    <div class="services__col">
      <div class="service service--gold">Introduction<br>to Power<br>boating</div>
      <div class="service service--dark">Open Water<br>Advanced<br>Maneuvers</div>
    </div>
    <div class="services__col">
      <div class="service service--dark">Precision<br>Docking &amp;<br>Boat Handling</div>
      <div class="service service--gold">Coastal<br>Navigation</div>
    </div>
    <div class="services__col">
      <div class="service service--gold">Open Water<br>Boat<br>Handling</div>
      <div class="service service--dark service--small">Captaining /<br>piloting Service<br>for Your Outings</div>
    </div>
  </div>
  <div class="back-url">www.helmandtide.com</div>
</section>

</body>
</html>
```